Design a styled business card for an intimacy and attachment psychologist

I am a Psychologist providing online therapy to patients across the United States. My work is interpersonal and emotion-focused, with an emphasis on the client-therapist relationship. My primary areas of work are very personal, including sexuality and gender, abuse and trauma, and grief and loss. My target audience will be adults of all ages 18+.
My business card should convey a warm and inviting feeling of professionalism that is also casual and comfortable.
The front should be fairly simple and professional, consisting of:
- My name, Dr. Rosalind Petrakis
- My title, Licensed Psycholigist
- My logo
On either the front or the back, my contact information should be listed:
- ros@drrospetrakis.example
- 555.014.7788
- drrospetrakis.example
On the rear, I would like a description of the areas that I specialize in. This can be formatted in any way that appears stylistically interesting.
Individual and Couples
Relationships and Infidelity
Sexual Health & Aging
Gender Identity & Sexual Orientation
Abuse and Trauma
Sexual Compulsivity & Addiction
Sexual Dysfunction
Target Market(s)
My target audience will be adults of all ages 18+.
Industry/Entity Type
Psychology
Contact Information for Business Card
The front should be fairly simple and professional, consisting of: - My name, Dr. Rosalind Petrakis - My title, Licensed Psycholigist - My logo On either the front or the back, my contact information should be listed: - ros@drrospetrakis.example - 555.014.7788 - drrospetrakis.example On the rear, I would like a description of the areas that I specialize in. This can be formatted in any way that appears stylistically interesting. Individual and Couples Relationships and Infidelity Sexual Health & Aging Gender Identity & Sexual Orientation Abuse and Trauma Sexual Compulsivity & Addiction Sexual Dysfunction
- Follow brand guide

```html
<!DOCTYPE html>
<html lang="en">
<head>
<meta charset="utf-8">
<title>Dr. Rosalind Petrakis – Business Card</title>
<link rel="stylesheet" href="https://fonts.googleapis.com/css2?family=Catamaran:wght@400;500;600;700&display=swap">
<style>
  :root {
    --page: #eef5f3;
    --teal: #62c4a9;
    --sunflower: #fdc35f;
    --ink: #2b2752;
    --white: #ffffff;
    --mint-soft: #e4f3ee;
  }
  * { box-sizing: border-box; margin: 0; padding: 0; }
  html, body {
    width: 1199px; height: 1200px; overflow: hidden;
    background: var(--page);
    font-family: "Catamaran", sans-serif;
  }
  .canvas { position: relative; width: 1199px; height: 1200px; }
  .card {
    position: absolute; left: 166px; width: 868px; height: 512px; overflow: hidden;
  }
  .card--front { top: 69px; background: var(--teal); }
  .card--back { top: 620px; background: var(--sunflower); }

  .brand { position: absolute; display: flex; align-items: center; gap: 22px; }
  .brand__disc {
    flex: none; border-radius: 50%;
    background: var(--mint-soft); border: 6px solid var(--ink);
  }
  .brand__name {
    color: var(--ink); font-weight: 700; text-transform: uppercase;
    line-height: 1.02; letter-spacing: 0.02em;
  }
  .card--front .brand { left: 57px; top: 54px; }
  .card--front .brand__disc { width: 120px; height: 120px; }
  .card--front .brand__name { font-size: 34px; }

  .identity { position: absolute; left: 58px; top: 256px; color: var(--white); }
  .identity__name { font-size: 29px; font-weight: 600; line-height: 1.2; }
  .identity__title { font-size: 20px; font-weight: 400; margin-top: 8px; }

  .contact {
    position: absolute; left: 58px; top: 362px; list-style: none;
    color: var(--white); font-size: 20px; line-height: 33px;
  }
  .contact li { display: flex; align-items: center; gap: 9px; }
  .contact svg { width: 16px; height: 16px; flex: none; }

  .rule {
    position: absolute; left: 351px; top: 447px; width: 445px; height: 3px;
    background: var(--white);
  }

  .card--back .brand {
    left: 90px; top: 112px; flex-direction: column; align-items: center; gap: 24px;
  }
  .card--back .brand__disc { width: 142px; height: 142px; }
  .card--back .brand__name { font-size: 36px; text-align: center; }

  .specialties {
    position: absolute; left: 468px; top: 126px; list-style: none;
    color: var(--ink); font-size: 20px; line-height: 39.6px;
  }
  .specialties li::before { content: "• "; }
</style>
</head>
<body>
<div class="canvas">

  <section class="card card--front" aria-label="Business card front">
    <div class="brand">
      <span class="brand__disc"></span>
      <span class="brand__name">Dr.<br>Rosalind<br>Petrakis</span>
    </div>

    <div class="identity">
      <p class="identity__name">Dr. Rosalind Petrakis</p>
      <p class="identity__title">Licensed Psycholigist</p>
    </div>

    <ul class="contact">
      <li>
        <svg viewBox="0 0 16 16" aria-hidden="true"><path fill="#fff" d="M4 1.5 6.2 4 5 5.6c.9 2 2.4 3.5 4.4 4.4L11 8.8l2.5 2.2-1.4 2.5C7 13.3 2.7 9 2.5 3.9Z"/></svg>
        555.014.7788
      </li>
      <li>
        <svg viewBox="0 0 16 16" aria-hidden="true"><rect x="1.5" y="3.5" width="13" height="9" fill="#fff"/><path d="M1.5 3.5 8 9l6.5-5.5" fill="none" stroke="#62c4a9" stroke-width="1.3"/></svg>
        ros@drrospetrakis.example
      </li>
      <li>
        <svg viewBox="0 0 16 16" aria-hidden="true"><circle cx="8" cy="8" r="6.5" fill="none" stroke="#fff" stroke-width="1.6"/><path d="M1.5 8h13M8 1.5c-3 3.5-3 9.5 0 13M8 1.5c3 3.5 3 9.5 0 13" fill="none" stroke="#fff" stroke-width="1.3"/></svg>
        drrospetrakis.example
      </li>
    </ul>

    <div class="rule"></div>
  </section>

  <section class="card card--back" aria-label="Business card back">
    <div class="brand">
      <span class="brand__disc"></span>
      <span class="brand__name">Dr.<br>Rosalind<br>Petrakis</span>
    </div>

    <ul class="specialties">
      <li>Individual and Couples</li>
      <li>Relationships and Infidelity</li>
      <li>Sexual Health &amp; Aging</li>
      <li>Gender Identity &amp; Sexual Orientation</li>
      <li>Abuse and Trauma</li>
      <li>Sexual Compulsivity &amp; Addiction</li>
      <li>Sexual Dysfunction</li>
    </ul>
  </section>

</div>
</body>
</html>
```